Copperfern Glen Retreat Wedding and Event Venue

We are looking for a webpage for our Wedding and Event Venue just opened up in Eastern San Diego CA. It is out of a private home that has a very photogenic backyard including grapevines and orchard trees, a 15 ft waterfall into a pool and market lights hanging from trees, all connected by paved stone and compacted dirt paths

We are looking for something that will be very bright, warm and inviting to our clients. The clientele will be mostly couples between 22 and 35 years of age for the weddings and planners/executives age 22-60 for our corporate events.

We would like a rustic Outdoor look as that is what our venue showcases. You can see our facebook Here: https://www.facebook.com/CopperfernGlenRetreat/

We would like for the pictures on the facebook to be used on the page. The google drive where most of them are located is here for full file sizes https://drive.examplecloud.net/open?id=7Q-9Kxw-M2pltR8TsUoLdE4-HJ6N

We would like to see designs that go with the colors of our logo and that included stone, wood, and grapevine textures as well as anything else rustic such as Market-lights.

The final design should be welcoming for newly engaged couples and corporations/companies who would like to book an outdoor venue for their wedding or next event. There can even be a simple first page with separate tabs for weddings and events that will be able to be more specially focused to the clients.

We would also like the option to be able to edit the pictures we place on the site seasonally as we would like our pictures to reflect our clients

Target Market(s)

Engaged couples age 22-35 and corporate planners/executives age 22-60

Industry/Entity Type

Events

Font styles to use
Script

Requirements
Must have
• Rustic Look, (wood, stone, wine vines/barrels, market lights, mason jars, etc)
• tab pages/sub pages for "About us", "Packages", "Pricing", "Gallery" (we must be able to put our pictures here from all our events), "What makes us Unique", "Contact us" that we are able to enter information into
Nice to have
• Colors matching our logo, Pictures from our Facebook page (listed in brief)
Should not have
• Corporate Look

```html
<!DOCTYPE html>
<html lang="en">
<head>
<meta charset="utf-8">
<title>Testimonials — Copperfern Glen Retreat</title>
<link rel="stylesheet" href="https://fonts.googleapis.com/css2?family=Cinzel:wght@400;600&family=Figtree:wght@400;500;600&family=Roboto:wght@300;400&display=swap">
<style>
  :root {
    --wood-light: #5a3520;
    --wood-mid: #3d2214;
    --wood-dark: #120a06;
    --gold: #c9a35a;
    --gold-footer: #b59a55;
    --cream: #f6efe2;
    --white: #ffffff;
    --divider: rgba(255,255,255,0.85);
  }
  * { box-sizing: border-box; margin: 0; padding: 0; }
  html, body { width: 1200px; height: 2466px; overflow: hidden; }
  body { background: var(--wood-dark); color: var(--white); font-family: "Figtree", sans-serif; }

  .site-header {
    position: relative; height: 222px;
    background: linear-gradient(90deg, #2b170d 0%, var(--wood-light) 30%, #4a2a18 55%, var(--wood-light) 75%, #2b170d 100%);
  }
  .brand {
    position: absolute; top: 56px; left: 0; right: 0; text-align: center;
    font-family: "Cinzel", serif; font-weight: 600; font-size: 30px; letter-spacing: 2px; color: var(--gold);
  }
  .brand-mark { display: inline-block; width: 14px; height: 14px; border-radius: 50%; background: var(--gold); margin-right: 12px; vertical-align: middle; }
  .main-nav {
    position: absolute; top: 145px; left: 85px; right: 85px; height: 49px;
    border-top: 1px dashed rgba(201,163,90,0.6); border-bottom: 1px dashed rgba(201,163,90,0.6);
    display: flex; justify-content: space-between; align-items: center; padding: 0 32px;
  }
  .main-nav a { font-family: "Cinzel", serif; font-size: 13px; color: var(--white); text-decoration: none; letter-spacing: 0.5px; }

  .hero { position: relative; height: 534px; }
  .hero-photo {
    position: absolute; inset: 0;
    background: linear-gradient(180deg, #d9d6cf 0%, #c8c2b6 40%, #9a5a55 62%, #b9aea0 85%, #cfc6b8 100%);
  }
  .hero-shade { position: absolute; inset: 0; background: rgba(0,0,0,0.18); }
  .hero-content { position: absolute; top: 240px; left: 0; right: 0; text-align: center; }
  .hero-title { font-family: "Cinzel", serif; font-weight: 600; font-size: 52px; letter-spacing: 1px; line-height: 56px; }
  .hero-sub { font-family: "Roboto", sans-serif; font-weight: 300; font-size: 18px; margin-top: 12px; }
  .hero-button {
    display: inline-block; margin-top: 22px; width: 171px; height: 46px; line-height: 44px;
    border: 2px solid var(--white); border-radius: 23px; background: rgba(0,0,0,0.15);
    font-family: "Cinzel", serif; font-size: 16px; color: var(--white); text-decoration: none;
  }

  .testimonials {
    position: relative; height: 1422px;
    background: linear-gradient(180deg, var(--wood-light) 0%, var(--wood-mid) 30%, #1e100a 60%, var(--wood-dark) 80%, #2a170e 100%);
  }
  .section-heading {
    position: absolute; top: 808px; top: 52px; left: 0; right: 0;
    display: flex; justify-content: center; align-items: center; gap: 18px;
    font-family: "Cinzel", serif; font-weight: 600; font-size: 25px; color: var(--gold); letter-spacing: 1px;
  }
  .section-heading .rule { width: 95px; height: 2px; background: linear-gradient(90deg, transparent, var(--gold)); }
  .section-heading .rule.right { background: linear-gradient(90deg, var(--gold), transparent); }
  .heading-ornament {
    position: absolute; top: 100px; left: 540px; width: 120px; height: 32px;
    background: radial-gradient(ellipse at center, rgba(201,163,90,0.75) 0%, rgba(201,163,90,0.2) 60%, transparent 75%);
  }
  .quote-list { position: absolute; top: 210px; left: 85px; right: 85px; }
  .quote {
    height: 307px; padding-top: 0; text-align: center; border-bottom: 1px dashed var(--divider);
  }
  .quote:last-child { border-bottom: none; }
  .quote + .quote { padding-top: 66px; }
  .quote blockquote { width: 780px; margin: 0 auto; font-size: 27px; line-height: 43px; font-weight: 500; }
  .quote cite { display: block; margin-top: 27px; font-style: normal; font-weight: 600; font-size: 19px; }

  .site-footer { position: relative; height: 288px; background: var(--gold-footer); text-align: center; }
  .footer-brand {
    position: absolute; top: 68px; left: 0; right: 0;
    font-family: "Cinzel", serif; font-weight: 600; font-size: 26px; letter-spacing: 2px; color: var(--cream);
  }
  .footer-rule { position: absolute; top: 148px; left: 85px; right: 85px; height: 1px; background: rgba(255,255,255,0.3); }
  .footer-nav { position: absolute; top: 176px; left: 0; right: 0; font-family: "Cinzel", serif; font-size: 13px; color: var(--white); }
  .footer-nav a { color: var(--white); text-decoration: none; }
  .footer-nav .sep { margin: 0 22px; }
  .copyright { position: absolute; top: 220px; left: 0; right: 0; font-family: Arial, sans-serif; font-size: 11px; color: var(--white); }
</style>
</head>
<body>
  <header class="site-header">
    <div class="brand"><span class="brand-mark"></span>Copperfern Glen Retreat</div>
    <nav class="main-nav">
      <a href="#">Home</a><a href="#">About Us</a><a href="#">Packages</a><a href="#">Pricing</a><a href="#">Gallery</a><a href="#">What Makes Us Unique</a><a href="#">Contact Us</a>
    </nav>
  </header>

  <section class="hero">
    <div class="hero-photo" role="img" aria-label="Wedding party photo: bride, groom, family and bridesmaids in red dresses under a white arched patio"></div>
    <div class="hero-shade"></div>
    <div class="hero-content">
      <h1 class="hero-title">TESTIMONIALS</h1>
      <p class="hero-sub">Sed ut perspiciatis unde omnis iste natus error sit voluptatem</p>
      <a class="hero-button" href="#">Read More</a>
    </div>
  </section>

  <section class="testimonials">
    <h2 class="section-heading"><span class="rule"></span>TESTIMONIALS<span class="rule right"></span></h2>
    <div class="heading-ornament" role="img" aria-label="Gold scroll ornament"></div>
    <div class="quote-list">
      <div class="quote">
        <blockquote>“Morbi in sem quis dui placerat ornare. Pellentesque odio nisi, euismod in, pharetra a, ultricies in, diam. Sed arcu. Cras consequat.”</blockquote>
        <cite>— MIRA, NEW YORK</cite>
      </div>
      <div class="quote">
        <blockquote>“Praesent dapibus, neque id cursus faucibus, tortor neque egestas augue, eu vulputate magna eros eu erat. Aliquam erat volutpat.”</blockquote>
        <cite>— MIRA, NEW YORK</cite>
      </div>
      <div class="quote">
        <blockquote>“Morbi in sem quis dui placerat ornare. Pellentesque odio nisi, euismod in, pharetra a, ultricies in, diam. Sed arcu. Cras consequat.”</blockquote>
        <cite>— MIRA, NEW YORK</cite>
      </div>
      <div class="quote">
        <blockquote>“Praesent dapibus, neque id cursus faucibus, tortor neque egestas augue, eu vulputate magna eros eu erat. Aliquam erat volutpat.”</blockquote>
        <cite>— MIRA, NEW YORK</cite>
      </div>
    </div>
  </section>

  <footer class="site-footer">
    <div class="footer-brand">Copperfern Glen Retreat</div>
    <div class="footer-rule"></div>
    <nav class="footer-nav">
      <a href="#">HOME</a><span class="sep">|</span><a href="#">ABOUT US</a><span class="sep">|</span><a href="#">PACKAGES</a><span class="sep">|</span><a href="#">PRICING</a><span class="sep">|</span><a href="#">GALLERY</a><span class="sep">|</span><a href="#">WHAT MAKES US UNIQUE</a><span class="sep">|</span><a href="#">CONTACT US</a>
    </nav>
    <p class="copyright">© Copyright 2017 Copperfern Glen.All Rights Reserved</p>
  </footer>
</body>
</html>
```